- Brightmoor Office Digest
- Links to the website
- I 'breathe fresh life' into office workplaces with these inspirational wellbeing newsletters! =)
- Other Facts

```html
<!DOCTYPE html>
<html lang="en">
<head>
<meta charset="utf-8">
<title>Brightmoor Office Digest</title>
<link rel="stylesheet" href="https://fonts.googleapis.com/css2?family=Barlow:wght@400;500;600;700&display=swap">
<style>
  :root {
    --page: #ffffff;
    --gold: #f2b705;
    --blue-top: #0858ab;
    --blue-bottom: #1a82cf;
    --green-top: #36a637;
    --green-bottom: #86c228;
    --orange: #ec7a1c;
    --bubble: #4ea6e0;
    --navy: #12305a;
    --ink: #1d2a12;
    --white: #ffffff;
    --photo-dark: #5a3a22;
    --photo-light: #c99a5a;
  }
  * { box-sizing: border-box; margin: 0; padding: 0; }
  html, body { width: 1200px; height: 960px; overflow: hidden; background: var(--page); }
  body { position: relative; font-family: "Barlow", Arial, sans-serif; }

  .newsletter { position: absolute; left: 186px; top: 67px; width: 814px; }

  .recipe {
    position: absolute; left: 0; top: 0; width: 814px; height: 389px;
    border-top: 4px solid var(--gold);
    background: linear-gradient(180deg, var(--blue-top), var(--blue-bottom));
    color: var(--white);
  }
  .recipe-title {
    position: absolute; left: 0; top: 10px; width: 814px; text-align: center;
    font-size: 36px; font-weight: 700; letter-spacing: 0.2px;
  }
  .section-heading {
    position: absolute; width: 200px; text-align: center;
    font-size: 18px; font-weight: 700; letter-spacing: 0.5px;
  }
  .heading-ingredients { left: 285px; top: 67px; }
  .heading-method { left: 283px; top: 167px; }
  .recipe-photo {
    position: absolute; left: 14px; top: 103px; width: 196px; height: 261px;
    background: radial-gradient(ellipse at 55% 70%, var(--photo-light), var(--photo-dark) 75%);
  }
  .ingredients {
    position: absolute; left: 233px; top: 104px; width: 545px;
    font-size: 13px; line-height: 17.5px;
  }
  .method {
    position: absolute; left: 233px; top: 188px; list-style: none;
    font-size: 13px; line-height: 17.5px;
  }
  .method li { position: relative; padding-left: 20px; }
  .method li span { position: absolute; left: 0; }
  .method .wide { width: 545px; }
  .method .narrow { width: 370px; }

  .joke-bubble {
    position: absolute; left: 608px; top: 207px; width: 172px; height: 172px;
    border-radius: 50%; border: 5px solid var(--white); background: var(--bubble);
    text-align: center; padding-top: 30px;
  }
  .joke-title { color: var(--navy); font-size: 20px; font-weight: 700; margin-bottom: 8px; }
  .joke-text { color: var(--white); font-size: 13px; font-weight: 700; line-height: 15.5px; }

  .events {
    position: absolute; left: 0; top: 389px; width: 814px; height: 371px;
    border-top: 4px solid var(--gold);
    background: linear-gradient(180deg, var(--green-top), var(--green-bottom));
    color: var(--ink);
  }
  .events-title {
    position: absolute; left: 0; top: 12px; width: 814px; text-align: center;
    color: var(--white); font-size: 36px; font-weight: 700;
  }
  .event-list { position: absolute; left: 64px; top: 72px; width: 712px; font-size: 13px; line-height: 19px; }
  .event { margin-bottom: 19px; }
  .event strong { font-weight: 700; }

  .quote-bar {
    position: absolute; left: 0; top: 764px; width: 814px; height: 58px;
    border: 5px solid var(--orange);
    background: linear-gradient(180deg, var(--blue-top), var(--blue-bottom));
    color: var(--white); font-size: 17px; font-weight: 700;
    display: flex; align-items: center; justify-content: center;
  }
</style>
</head>
<body>
<main class="newsletter">
  <section class="recipe">
    <h1 class="recipe-title">Tasty Tuscan Chicken</h1>
    <h2 class="section-heading heading-ingredients">INGREDIENTS</h2>
    <div class="recipe-photo" role="img" aria-label="Photo of grilled chicken breast served with beans and greens"></div>
    <p class="ingredients">1 punnet grape tomatoes, ½ cup (50g) pimento stuffed green olives, 2 tbs olive oil, juice of ½ lemon, 2 chicken breast fillets, 1tbs capers, ½ cup rice, basil leaves, brown rice and green salad to serve.</p>
    <h2 class="section-heading heading-method">METHOD</h2>
    <ol class="method">
      <li class="wide"><span>1.</span>Preheat oven to 180°C. Combine tomatoes, olives, capers, olive oil and lemon juice in a bowl.</li>
      <li class="narrow"><span>2.</span>Season chicken to taste and fry in a non stick pan for 3 minutes each side, until golden brown. Transfer to a baking pan.</li>
      <li class="narrow"><span>3.</span>Pour the tomato mixture over the chicken in the baking pan and season to taste. Bake for 15 minutes.</li>
      <li class="narrow"><span>4.</span>Top with a few basil leaves and serve with brown rice and green salad leaves.</li>
    </ol>
    <div class="joke-bubble">
      <p class="joke-title">HaHaHa</p>
      <p class="joke-text">“Waiter!<br>This coffee<br>tastes like mud.”<br>“Yes sir, it’s fresh<br>ground.”</p>
    </div>
  </section>

  <section class="events">
    <h2 class="events-title">What’s on this weekend?</h2>
    <div class="event-list">
      <p class="event"><strong>Sydney 28th Harbourside Quay Christmas Concert</strong> A family concert with performances from The Pocket Puppets. Exhibition Hall Forecourt, Harbourside Quay from 8pm, free.</p>
      <p class="event"><strong>Melbourne 28th and 29th November City Dash</strong> The exciting physical and mental urban adventure challenge is back on 28-29 November when teams of three will run, ride, kayak, climb and abseil across a course that’s only revealed to them hours before they begin. For more information call 1800 555 012.</p>
      <p class="event"><strong>Canberra 28 &amp; 29th Valley Fields Festival</strong> On Saturday 28 November, the Big 21st Birthday Bash Street Party will be held in Marlow Street. On Sunday 29 November, The Valley Fields Festival will celebrate 21 years with a free festival featuring live music, a children’s show, skateboarding and rollerblading, fireworks, market stalls and more in Valley Fields Town Park.</p>
      <p class="event"><strong>Brisbane 28 &amp; 29 Santa Celebration</strong> Activities include a jumping castle, a train simulator, art and craft, a screening of the Snowline Express and more. There will also be a visit from Santa. Activities are free after general museum entry. The Railyard Heritage Museum, Depot St, East Brookfield.</p>
    </div>
  </section>

  <footer class="quote-bar">“There are no shortcuts to any place worth going” Vera Lindqvist</footer>
</main>
</body>
</html>
```